IT Services Business Card Design

We require a business card design for an IT services company called RT Code Transit.

We specialize in taking an organisations software and readying it for deployment to new environments (e.g. Nex 3 to Nex 5). This process is termed application packaging. This is not the same as putting things in boxes but I am happy to use boxes as a pun icon ;-) This is our second step in branding, we currently have a new logo and our poor excuse of a website is next to be updated but it contains information on who we are and what we cover at rtcodetransit.example

We are looking for a fun, modern but stylish and professional looking design.

I have attached the logo in multiple formats including vector formats (and the fonts that created the logo if required)
Updates

Thanks to all the designers so far, some great designs in there.  I will be selecting a card design on the deadline date. 

However, there is still time to submit some more designs.  The majority of the ones I have so far are typical simplistic designs that we have all seen before and I have enough of those to choose from now.  If you wish to submit any more designs, please submit somthing unusual to grab our attention.

Target Market(s)

Project executives of large organisations looking for Nexora migrations

Industry/Entity Type

Software

Requirements
Must have
• Want to show company name, contact name, title, main number, contact number, fax number, email address and website address. I do not want to show the address.
Must use the attached logo, retaining the colours in them.

This has to be a double-sided design. I will be using pelby.example and will be selecting their rounded corner business card design.

Their templates and design requirements (sizing etc.) can be found here: http://uk.pelby.example/help/faq/templates-and-guidelines.html

Happy for company name or website to be on either side of the card.

This design has to be original and not used before for another company

Would like to style it around the business colours in the logo
Nice to have
• Pelby.example has an option for multiple card designs to appear on the back. If this is possible in the budget and time you have and you have a design(s) that work with that but carry the same style and theme, that would be nice to see but not necessary.
Should not have
• We do not want to put a postal address on the cards

```html
<!DOCTYPE html>
<html lang="en">
<head>
<meta charset="utf-8">
<title>RT Code Transit – Business Card</title>
<link rel="stylesheet" href="https://fonts.googleapis.com/css2?family=Questrial&display=swap">
<style>
  :root {
    --page-bg: #e7e4e0;
    --card-white: #ffffff;
    --card-charcoal: #2e322e;
    --panel-dark: #45413b;
    --panel-mid: #7d786f;
    --ink: #3b3a38;
    --ink-soft: #555350;
    --brand-blue: #5a7be0;
    --light-text: #f4f4f2;
  }
  html, body {
    margin: 0;
    width: 1200px;
    height: 900px;
    overflow: hidden;
    background: var(--page-bg);
  }
  .stage {
    position: relative;
    width: 1200px;
    height: 900px;
  }
  .card {
    position: absolute;
    left: 300px;
    width: 600px;
    height: 388px;
    border-radius: 26px;
    overflow: hidden;
    box-shadow: 0 6px 18px rgba(0,0,0,0.18);
  }
  .card--back { top: 40px; background: var(--card-charcoal); }
  .card--front { top: 472px; background: var(--card-white); }
  .card svg { display: block; }
  .type {
    font-family: "Questrial", "Century Gothic", sans-serif;
  }
  .brand-name--back { fill: #d9d9d6; font-size: 34px; }
  .brand-name--front { fill: var(--ink); font-size: 24px; }
  .holder-name { fill: var(--ink); font-size: 31px; }
  .holder-title { fill: var(--ink-soft); font-size: 14px; }
  .contact-line { fill: var(--light-text); font-size: 19px; }
  .contact-link { fill: var(--light-text); font-size: 15px; }
</style>
</head>
<body>
<main class="stage">

  <section class="card card--back" aria-label="Card back">
    <svg width="600" height="388" viewBox="0 0 600 388">
      <g class="brand-lockup">
        <circle cx="130" cy="194" r="16" fill="var(--brand-blue)"/>
        <text class="type brand-name--back" x="160" y="206">RT Code Transit</text>
      </g>
    </svg>
  </section>

  <section class="card card--front" aria-label="Card front">
    <svg width="600" height="388" viewBox="0 0 600 388">
      <defs>
        <linearGradient id="panelShade" x1="0" y1="0" x2="1" y2="1">
          <stop offset="0" stop-color="var(--panel-mid)"/>
          <stop offset="1" stop-color="var(--panel-dark)"/>
        </linearGradient>
      </defs>

      <polygon class="accent-panel" role="img" aria-label="Decorative light-ray graphic area"
               points="0,28 600,388 0,388" fill="url(#panelShade)"/>

      <g class="brand-lockup">
        <text class="type brand-name--front" x="520" y="70" text-anchor="end">RT Code Transit</text>
        <circle cx="548" cy="62" r="16" fill="var(--brand-blue)"/>
      </g>

      <text class="type holder-name" x="560" y="158" text-anchor="end">Your Long Name</text>
      <text class="type holder-title" x="560" y="180" text-anchor="end">Job Title</text>

      <text class="type contact-line" x="30" y="264">Tel&#160;&#160;0845 000 1274</text>
      <text class="type contact-line" x="30" y="290">Fax 0872 000 5583</text>
      <text class="type contact-link" x="30" y="334">www.rtcodetransit.example</text>
      <text class="type contact-link" x="30" y="358">Enquiries@RTCodeTransit.example</text>
    </svg>
  </section>

</main>
</body>
</html>
```